Business Cards for an 'affordable luxury' inner city home builder in Calgary.

We need a business card design that emulates the progressive, innovative, culture of our company and the modern style of our homes. Use our website www.velmarbuilds-ex.com as a reference for the product we build.

Our company builds homes in the inner city space of Calgary, Alberta. We build affordable luxury.

Target Market(s)

Young professional Families

Contact Information for Business Card

Try to maintain consistency with the logo font and the card font.

Requirements
Must have
• The details must include: Name, education, title, phone number, website and email (Address is not as important)
• The design must be uniques (like our logo), elegant, sophisticated and modern.

```html
<!DOCTYPE html>
<html lang="en">
<head>
<meta charset="utf-8">
<title>Velmar Builds Ltd — Business Cards</title>
<link rel="stylesheet" href="https://fonts.googleapis.com/css2?family=Montserrat:wght@500;600&family=Open+Sans:wght@400;600;700&display=swap">
<style>
  :root {
    --backdrop: #1c1c1d;
    --card: #262627;
    --card-edge: #2e2e2f;
    --silver: #a9a9ab;
    --white: #f4f4f4;
    --muted: #d8d8d8;
    --rule: #cfcfcf;
  }
  * { margin: 0; padding: 0; box-sizing: border-box; }
  html, body {
    width: 1200px;
    height: 895px;
    overflow: hidden;
    background: var(--backdrop);
  }
  .sheet {
    width: 1200px;
    height: 895px;
    display: flex;
    flex-direction: column;
    align-items: center;
    justify-content: center;
    gap: 40px;
  }
  .card {
    position: relative;
    width: 620px;
    height: 354px;
    background: var(--card);
    border: 1px solid var(--card-edge);
    border-radius: 18px;
    box-shadow: 0 14px 30px rgba(0,0,0,0.55);
    color: var(--white);
  }

  /* Front */
  .brand {
    position: absolute;
    left: 150px;
    top: 92px;
    display: flex;
    align-items: flex-end;
    gap: 22px;
  }
  .brand-square {
    width: 64px;
    height: 64px;
    background: #1e1e1f;
    flex: none;
  }
  .brand-name {
    font-family: "Montserrat", sans-serif;
    font-weight: 500;
    font-size: 34px;
    line-height: 1.0;
    letter-spacing: 2px;
    color: var(--silver);
    text-transform: uppercase;
  }
  .front-url {
    position: absolute;
    left: 0;
    right: 0;
    bottom: 48px;
    text-align: center;
    font-family: "Open Sans", sans-serif;
    font-weight: 700;
    font-size: 15px;
    letter-spacing: 1.5px;
    color: var(--white);
  }

  /* Back */
  .back-content {
    position: absolute;
    left: 0;
    right: 0;
    top: 118px;
    display: flex;
    justify-content: center;
    align-items: center;
    gap: 26px;
  }
  .identity {
    text-align: right;
  }
  .person-name {
    font-family: "Montserrat", sans-serif;
    font-weight: 600;
    font-size: 23px;
    letter-spacing: 1px;
    text-transform: uppercase;
    color: var(--white);
    margin-bottom: 4px;
  }
  .person-detail {
    font-family: "Open Sans", sans-serif;
    font-size: 14px;
    line-height: 1.35;
    color: var(--muted);
  }
  .divider {
    width: 1px;
    height: 84px;
    background: var(--rule);
  }
  .contact-list {
    list-style: none;
    font-family: "Open Sans", sans-serif;
    font-size: 14px;
    color: var(--muted);
    letter-spacing: 0.3px;
  }
  .contact-list li {
    display: flex;
    align-items: center;
    gap: 12px;
    height: 24px;
  }
  .contact-list svg {
    width: 14px;
    height: 14px;
    flex: none;
  }
</style>
</head>
<body>
  <main class="sheet">
    <section class="card card-front" aria-label="Card front">
      <div class="brand">
        <span class="brand-square" aria-hidden="true"></span>
        <h1 class="brand-name">Velmar<br>Builds<br>Ltd</h1>
      </div>
      <p class="front-url">www.velmarbuilds-ex.com</p>
    </section>

    <section class="card card-back" aria-label="Card back">
      <div class="back-content">
        <div class="identity">
          <h2 class="person-name">Adrian Kessler</h2>
          <p class="person-detail">M.Sc. in Architecture<br>Founder &amp; CEO</p>
        </div>
        <span class="divider" aria-hidden="true"></span>
        <ul class="contact-list">
          <li>
            <svg viewBox="0 0 14 14" aria-hidden="true"><rect x="3.5" y="0.8" width="7" height="12.4" rx="1.4" fill="none" stroke="#e6e6e6" stroke-width="1.3"/><circle cx="7" cy="11" r="0.8" fill="#e6e6e6"/></svg>
            <span>403-555-0148</span>
          </li>
          <li>
            <svg viewBox="0 0 14 14" aria-hidden="true"><rect x="0.8" y="2.8" width="12.4" height="8.4" fill="none" stroke="#e6e6e6" stroke-width="1.3"/><path d="M1 3.2 L7 8 L13 3.2" fill="none" stroke="#e6e6e6" stroke-width="1.3"/></svg>
            <span>projects@velmarbuilds-ex.com</span>
          </li>
          <li>
            <svg viewBox="0 0 14 14" aria-hidden="true"><circle cx="7.5" cy="6" r="4.6" fill="none" stroke="#e6e6e6" stroke-width="1.4"/><path d="M4.2 9.4 L1.2 12.8" stroke="#e6e6e6" stroke-width="1.6"/></svg>
            <span>www.velmarbuilds-ex.com</span>
          </li>
        </ul>
      </div>
    </section>
  </main>
</body>
</html>
```